Postcard flyer for body postive dance classes

We need an eye catching double sided A6 postcard for body positive dance classes. The business name is stepbloomjoy and already have a rough logo and some text that needs tidying up and putting together. The design needs to be simple and elegant. We are appealing to a diverse range of adult women with or without dance experience to join us in a safe, supportive and creative environment. We would like the design to use black, white and a soft green. The final design should communicate movement, contentment and wholeness. File with information attached.

Target Market(s)

Diverse range of adult women

Industry/Entity Type

Health And Wellness

Font styles to use
Other font styles liked:
• Candara or similar but open to suggestions

Colors
abd036
cadf82
eaf2ce
fffefb
fef9ed
fff3d1
ffffff

Requirements
Must have
• Logo and text provided.
Nice to have
• Sense of movement. Match to website colours and style.
Should not have
• Intimidating perfect body images

```html
<!DOCTYPE html>
<html lang="en">
<head>
<meta charset="utf-8">
<title>stepbloomjoy postcard</title>
<link rel="stylesheet" href="https://fonts.googleapis.com/css2?family=Cabin:wght@400;500;600;700&family=Open+Sans:wght@600;700&display=swap">
<style>
:root{
  --stage:#9a9797;
  --green:#abd036;
  --green-soft:#cadf82;
  --ink:#111111;
  --charcoal:#3d3d3f;
  --grey-dark:#454547;
  --grey-mid:#6d6d6d;
  --white:#ffffff;
  --stamp:#e6e6e7;
}
*{margin:0;padding:0;box-sizing:border-box}
html,body{width:872px;height:1200px;overflow:hidden;background:var(--stage)}
body{position:relative;font-family:"Cabin",Candara,sans-serif;color:var(--white)}
.card{position:absolute;width:745px;height:528px;overflow:hidden;box-shadow:6px 8px 14px rgba(0,0,0,.35)}
.card-front{left:72px;top:38px;background:radial-gradient(ellipse at 55% 35%,#7a7a7a 0%,#5a5a5a 45%,#3a3a3a 100%)}
.card-back{left:70px;top:623px;background:var(--white)}

/* front */
.hero-dancer{position:absolute;left:30px;top:0;width:230px;height:496px;background:linear-gradient(180deg,#8d8d8d 0%,#b3b3b3 45%,#8a8a8a 100%);border-radius:0 0 40px 40px;opacity:.85}
.brand-mark{position:absolute;left:390px;top:52px;width:200px;text-align:center;font-size:18px;font-weight:600;color:var(--ink)}
.title-band{position:absolute;left:0;top:0}
.headline{position:absolute;left:245px;top:102px;width:480px;text-align:center;font-family:"Open Sans",sans-serif;font-weight:700;font-size:47px;letter-spacing:.5px;color:var(--green)}
.tagline{position:absolute;left:245px;top:168px;width:480px;text-align:center;font-family:"Open Sans",sans-serif;font-weight:600;font-size:24px}
.intro{position:absolute;left:250px;top:214px;width:470px;text-align:center;font-size:15.5px;line-height:26px}
.intro p+p{margin-top:6px}
.thumb{position:absolute;top:379px;width:137px;height:83px;border:3px solid var(--white);background:linear-gradient(135deg,#e8e8e8 0%,#a9a9a9 55%,#5d5d5d 100%);box-shadow:0 10px 12px rgba(0,0,0,.45)}
.thumb-1{left:260px}.thumb-2{left:421px}.thumb-3{left:575px}
.front-footer{position:absolute;left:0;bottom:0;width:100%;height:32px;background:var(--ink)}
.social{position:absolute;left:30px;top:7px;display:flex;gap:8px}
.social span{width:18px;height:18px;border-radius:50%;background:#f3eed8}
.web{position:absolute;left:372px;top:5px;font-size:17px;letter-spacing:.3px}

/* back */
.back-panel{position:absolute;left:0;top:0;width:415px;height:528px;background:var(--grey-dark)}
.back-photo{position:absolute;left:0;top:0;width:415px;height:265px;background:linear-gradient(180deg,#d9d9d9 0%,#9c9c9c 45%,#4b4b4b 100%)}
.back-wordmark{position:absolute;left:40px;top:4px;font-size:22px;line-height:26px;color:var(--white);opacity:.9}
.classes-tab{position:absolute;left:0;top:226px}
.classes-tab-label{position:absolute;left:8px;top:229px;font-family:"Open Sans",sans-serif;font-weight:700;font-size:22px;color:var(--white)}
.classes{position:absolute;left:0;top:266px;width:415px;height:68px;display:flex;background:var(--charcoal)}
.class{flex:1;text-align:center;padding-top:6px;font-size:14.5px;line-height:18px}
.class+.class{border-left:1px solid #8a8a8a}
.class h3{font-family:"Open Sans",sans-serif;font-weight:700;font-size:16px;line-height:22px}
.motto{position:absolute;left:0;top:342px;width:415px;height:42px;background:var(--ink);text-align:center;font-family:"Open Sans",sans-serif;font-weight:600;font-size:15.5px;line-height:42px}
.contact{position:absolute;left:0;top:394px;width:415px;text-align:center}
.contact h3{font-family:"Open Sans",sans-serif;font-weight:600;font-size:20px;line-height:26px}
.contact .area{font-weight:700;font-size:17px;line-height:26px}
.contact .phone{position:absolute;left:90px;top:54px;display:flex;align-items:center;gap:28px;font-family:"Open Sans",sans-serif;font-weight:700;font-size:19px}
.contact .mail{position:absolute;left:90px;top:86px;display:flex;align-items:center;gap:12px;font-size:14.5px}
.back-footer{position:absolute;left:0;bottom:0;width:415px;height:22px;background:var(--ink);text-align:center;font-size:15px;line-height:22px}
.address-name{position:absolute;left:431px;top:41px;font-family:"Open Sans",sans-serif;font-weight:700;font-size:20px;color:var(--green)}
.stamp{position:absolute;left:647px;top:15px;width:80px;height:81px;background:var(--stamp)}
</style>
</head>
<body>

<section class="card card-front">
  <div class="hero-dancer" role="img" aria-label="Black and white photo of a dancer holding a high standing leg extension"></div>
  <div class="brand-mark">stepbloomjoy</div>
  <svg class="title-band" width="745" height="528" aria-hidden="true">
    <polygon points="240,106 735,106 725,176 240,176" fill="#ffffff" fill-opacity=".08"/>
  </svg>
  <h1 class="headline">STEPBLOOMJOY</h1>
  <p class="tagline">movement, contentment, wholeness</p>
  <div class="intro">
    <p>Dance is joy, dance is love. Dance is at the core of our being,<br>a celebration of movement, vitality and wholeness.</p>
    <p>If you've never danced before and always wanted to or you<br>want to reignite your past love of dance, join us at stepbloomjoy<br>to start your journey.</p>
  </div>
  <div class="thumb thumb-1" role="img" aria-label="Photo of a dancer stretching at the barre"></div>
  <div class="thumb thumb-2" role="img" aria-label="Photo of dancers in a bright studio"></div>
  <div class="thumb thumb-3" role="img" aria-label="Photo of a dancer with leg raised on the barre"></div>
  <footer class="front-footer">
    <div class="social" aria-label="Social links"><span></span><span></span><span></span></div>
    <span class="web">www.stepbloomjoy.com.au</span>
  </footer>
</section>

<section class="card card-back">
  <div class="back-panel">
    <div class="back-photo" role="img" aria-label="Black and white photo of a dancer in a studio with leg extended"></div>
    <span class="back-wordmark">stepbloomjoy</span>
    <svg class="classes-tab" width="180" height="32" aria-hidden="true">
      <polygon points="0,0 180,0 166,32 0,32" fill="#abd036"/>
    </svg>
    <h2 class="classes-tab-label">OUR CLASSES</h2>
    <div class="classes">
      <div class="class"><h3>FLOW I</h3>Wednesday 11-12pm<br>Saturdays 12-1pm</div>
      <div class="class"><h3>FLOW II</h3>Wednesday 12-1pm</div>
      <div class="class"><h3>FLOW III</h3>Saturday 1-2pm</div>
    </div>
    <p class="motto">FLOW WITH LIFE THROUGH YOUR INNER DANCER.</p>
    <div class="contact">
      <h3>CONTACT US</h3>
      <p class="area">Northvale/Eastbrook</p>
      <p class="phone">
        <svg width="16" height="16" viewBox="0 0 16 16" aria-hidden="true"><circle cx="8" cy="8" r="7" fill="none" stroke="#fff" stroke-width="1.4"/><path d="M5.5 4.5c.5-.5 1-.5 1.3 0l.6 1c.2.4 0 .7-.3 1l-.3.3c.4.9 1.1 1.6 2 2l.3-.3c.3-.3.6-.5 1-.3l1 .6c.5.3.5.8 0 1.3-.7.7-1.600.8-2.6.2A7 7 0 0 1 5.3 7c-.5-1-.5-1.8.2-2.5z" fill="#fff"/></svg>
        0400517286
      </p>
      <p class="mail">
        <svg width="12" height="9" viewBox="0 0 12 9" aria-hidden="true"><rect width="12" height="9" fill="#fff"/><path d="M0 0l6 5 6-5" fill="none" stroke="#454547" stroke-width="1.2"/></svg>
        mara@stepbloomjoy.com.au
      </p>
    </div>
    <footer class="back-footer">www.stepbloomjoy.com.au</footer>
  </div>
  <p class="address-name">STEPBLOOMJOY</p>
  <div class="stamp" aria-label="Stamp area"></div>
</section>

</body>
</html>
```